Service company standing banner design

We are an existing company that just updated our logo. We are attending some oportunity summits in the near future and want a new crisp clean look on our three banners that will be placed in the back of our small booth. The summits we are attending are designed to give local companies opportunities on a prokect we have been awarded to construct in their area. These banners should communicate who we are with no questions when people see them. One banner shall list our services. One to list our values and one to state our goals. All these while being appealing to the eye and using picture of nature. Attached are copies of what we are to replace. also the new logo and the original background pictures in the existing banners

```html
<!DOCTYPE html>
<html lang="en">
<head>
<meta charset="utf-8">
<title>Tessel Services – Booth Banners</title>
<link rel="stylesheet" href="https://fonts.googleapis.com/css2?family=Montserrat:wght@500;600;700&display=swap">
<style>
  :root {
    --page-bg: #f3f3f3;
    --brand-blue: #154a9c;
    --brand-orange: #f47a20;
    --white: #ffffff;
  }
  * { margin: 0; padding: 0; box-sizing: border-box; }
  html, body { width: 1200px; height: 1200px; overflow: hidden; }
  body {
    background: var(--page-bg);
    font-family: "Montserrat", Arial, sans-serif;
    position: relative;
  }
  .banner {
    position: absolute;
    top: 153px;
    width: 384px;
    height: 893px;
    box-shadow: 0 6px 18px rgba(0,0,0,0.08);
    overflow: hidden;
  }
  .banner--goals { left: 0; }
  .banner--services { left: 408px; }
  .banner--values { left: 816px; }

  .banner__photo { position: absolute; inset: 0; }
  .photo--forest-river {
    background: linear-gradient(180deg, #2c4a2e 0%, #3d5f38 35%, #2e4a2c 60%, #6b7468 78%, #b9d6de 88%, #8a8680 100%);
  }
  .photo--snow-forest {
    background: linear-gradient(180deg, #4f6aa6 0%, #8898c2 25%, #b9c4dd 42%, #e6ebf3 60%, #f4f6fa 80%, #e9edf4 100%);
  }
  .photo--lake-forest {
    background: linear-gradient(180deg, #3a4a34 0%, #2c3f2a 30%, #2b4a3a 42%, #2c7a78 52%, #4f9a98 62%, #8a8a5a 78%, #9a8a5c 100%);
  }

  .brand-box {
    position: absolute;
    left: 68px;
    top: 0;
    width: 248px;
    height: 97px;
    background: var(--white);
    display: flex;
    align-items: center;
    justify-content: center;
    gap: 10px;
  }
  .brand-box__dot {
    width: 30px; height: 30px;
    border-radius: 50%;
    background: var(--brand-orange);
    flex: none;
  }
  .brand-box__name {
    color: var(--brand-blue);
    font-weight: 700;
    font-size: 16px;
    line-height: 1.1;
  }
  .brand-box__name span { display: block; font-size: 12.5px; }

  .info-panel {
    position: absolute;
    left: 68px;
    bottom: 0;
    width: 248px;
    background: var(--brand-blue);
    color: var(--white);
    text-align: center;
    display: flex;
    flex-direction: column;
    align-items: center;
  }
  .banner--goals .info-panel { top: 398px; padding-top: 26px; }
  .banner--services .info-panel { top: 244px; padding-top: 30px; }
  .banner--values .info-panel { top: 457px; padding-top: 32px; }

  .info-panel__title {
    color: var(--brand-orange);
    font-weight: 700;
    font-size: 37px;
    line-height: 1.1;
    letter-spacing: -0.5px;
  }
  .goal-lead {
    margin-top: 24px;
    font-weight: 600;
    font-size: 19.5px;
    line-height: 27px;
  }
  .goal-body {
    margin-top: 30px;
    font-weight: 500;
    font-size: 19.5px;
    line-height: 27px;
    padding: 0 14px;
  }
  .service-list, .value-list { list-style: none; }
  .service-list { margin-top: 26px; }
  .service-list li {
    font-weight: 600;
    font-size: 21px;
    line-height: 23px;
    margin-bottom: 23px;
  }
  .value-list { margin-top: 26px; }
  .value-list li {
    font-weight: 600;
    font-size: 28px;
    line-height: 34px;
    margin-bottom: 18px;
  }
  .panel-mark {
    position: absolute;
    bottom: 34px;
    left: 50%;
    width: 46px; height: 46px;
    margin-left: -23px;
    border-radius: 50%;
    background: var(--brand-orange);
  }
</style>
</head>
<body>

<section class="banner banner--goals">
  <div class="banner__photo photo--forest-river" role="img" aria-label="Photo of an evergreen forest above a rocky rushing river"></div>
  <div class="brand-box">
    <div class="brand-box__dot"></div>
    <div class="brand-box__name">Tessel Services<span>Limited Partnership</span></div>
  </div>
  <div class="info-panel">
    <h2 class="info-panel__title">Goals</h2>
    <p class="goal-lead">Honouring the<br>interests of<br>indigenous people</p>
    <p class="goal-body">To build and grow a strong regional busniess providing the best quality for our people and clients.</p>
    <div class="panel-mark"></div>
  </div>
</section>

<section class="banner banner--services">
  <div class="banner__photo photo--snow-forest" role="img" aria-label="Photo of snow-covered spruce trees and a snowy field under a blue sky"></div>
  <div class="brand-box">
    <div class="brand-box__dot"></div>
    <div class="brand-box__name">Tessel Services<span>Limited Partnership</span></div>
  </div>
  <div class="info-panel">
    <h2 class="info-panel__title">Services</h2>
    <ul class="service-list">
      <li>Pipeline<br>Construction</li>
      <li>Pipeline<br>Clearning</li>
      <li>Civil Works</li>
      <li>Land Clearning</li>
      <li>Road<br>Maintenance</li>
      <li>Relcamation</li>
      <li>Logging</li>
      <li>Mulching</li>
    </ul>
    <div class="panel-mark"></div>
  </div>
</section>

<section class="banner banner--values">
  <div class="banner__photo photo--lake-forest" role="img" aria-label="Photo of a dense conifer forest above a turquoise river with grassy banks"></div>
  <div class="brand-box">
    <div class="brand-box__dot"></div>
    <div class="brand-box__name">Tessel Services<span>Limited Partnership</span></div>
  </div>
  <div class="info-panel">
    <h2 class="info-panel__title">Values</h2>
    <ul class="value-list">
      <li>Integrity</li>
      <li>Transparency</li>
      <li>Respect</li>
      <li>Trust</li>
    </ul>
    <div class="panel-mark"></div>
  </div>
</section>

</body>
</html>
```